Attention Getting Doorhanger Postcard Campaign offering HUGE Rebate on New Construction Homes

I am reestablishing my real estate career in the far North Dallas, TX area and want to offer a rebate on new construction homes to help get me started. I am requesting a doorhanger as my first project but would like a theme that I can carry over to other projects including postcards and other marketing items. I want it to look high end, clean, professional and classy. I am attaching a copy of a flier that I created that needs (no graphic designer here) some prettying up. But this is just to give you an idea of the type of style that is of interest to me.

Target Market(s)

Home buyers for new construction in far north dallas suburbs. Usually a move up buyer.

Industry/Entity Type

Real Estate

Colors

Designer to choose colors to be used in the design.

Requirements
Must have
• Catch phrase, draw attention, classy clean lines, current trend colors of blues and grays. My information, Harwood Fenn logo, equal housing and realtor logos. Fine Print: Not intended to solicit homes already listed for sale or buyers already in a buyers agency agreement with another brokerage. Please include offer details as listed in my flier. Again I am interested in a door hanger and the next round would be a flier or postcard.
Nice to have
• Picture of new homes that are in line with what is being built in my area. A few home builders sites: Silver Meadow, Brookvale Homes, Tenbury Homes, Calloway Homes.

```html
<!DOCTYPE html>
<html lang="en">
<head>
<meta charset="utf-8">
<title>Door Hanger – New Construction Rebate</title>
<link rel="stylesheet" href="https://fonts.googleapis.com/css2?family=Montserrat:ital,wght@0,400;0,500;0,600;0,700;0,800;1,500;1,700&family=Allura&display=swap">
<style>
  :root{
    --page:#eef0f3;
    --blue:#0b5cb8;
    --blue-deep:#0a4a9a;
    --blue-sky:#1f6fd0;
    --blue-light:#7fc1ff;
    --blue-pale:#cde8fb;
    --ink:#1c1f26;
    --red:#c8102e;
    --white:#ffffff;
  }
  *{box-sizing:border-box;margin:0;padding:0}
  html,body{width:1200px;height:1000px;overflow:hidden;background:var(--page)}
  body{font-family:"Montserrat",Arial,sans-serif;color:var(--ink);position:relative}
  .hanger{position:absolute;top:60px;width:340px;height:880px;overflow:hidden;box-shadow:0 6px 18px rgba(0,0,0,.18)}
  .hanger--front{left:245px;background:var(--white)}
  .hanger--back{left:615px;background:var(--blue-pale)}
  .hole{position:absolute;left:50%;top:120px;width:84px;height:84px;margin-left:-42px;border-radius:50%;background:var(--page);z-index:3}
  .sky{position:absolute;left:0;top:0;width:100%;height:220px;background:linear-gradient(180deg,#0a56b5,var(--blue-sky))}
  .photo{position:absolute;left:0;width:100%}
  .hanger--front .photo{top:210px;height:220px;background:linear-gradient(180deg,#2c6fc4 0%,#8a7f74 45%,#5c5a52 70%,#3f6b2e 100%)}
  .hanger--back .photo{top:0;height:420px;background:linear-gradient(180deg,#b8c2df 0%,#e8d9df 35%,#f1f0ee 55%,#c9ccc8 72%,#4f7a3a 100%)}
  .band{position:absolute;left:0;width:100%;background:var(--blue);color:var(--white)}
  .hanger--front .band{top:430px;height:158px;border-bottom:6px solid var(--blue-sky)}
  .hanger--back .band{top:420px;height:148px;border-bottom:6px solid var(--blue-sky);padding:12px 14px 0 14px}
  .headline{display:flex;align-items:flex-end;justify-content:center;gap:6px;margin-top:10px}
  .headline .big{font-weight:800;font-size:40px;letter-spacing:1px;line-height:1}
  .headline .stack{display:flex;flex-direction:column;align-items:flex-start;line-height:1}
  .headline .small{font-style:italic;font-weight:500;font-size:17px;margin-left:6px}
  .offer{text-align:center;margin-top:10px;font-weight:600;font-size:16px}
  .offer-row{display:flex;align-items:center;justify-content:center;gap:4px;margin-top:0}
  .offer-pct{font-weight:800;font-size:38px;color:var(--blue-light);line-height:1}
  .offer-text{font-size:12px;font-weight:500;text-align:left;line-height:1.2}
  .offer-text strong{font-weight:800}
  .savings{position:absolute;top:604px;left:0;width:100%;text-align:center}
  .pill{display:inline-block;background:var(--blue-sky);color:var(--white);font-weight:800;font-size:17px;padding:3px 10px;border:2px solid var(--blue-deep);border-radius:3px}
  .savings p{font-size:12px;font-weight:600;margin-top:6px;line-height:1.25}
  .savings .accent{color:var(--blue);font-weight:800;font-size:14px}
  .savings .label{color:var(--blue);font-weight:800;font-size:15px;margin-top:2px}
  .agent{position:absolute;top:706px;left:14px;right:10px;display:flex;gap:10px}
  .portrait{width:128px;height:160px;border:3px solid var(--blue);background:linear-gradient(180deg,#3d5f8a,#6b5a4c 60%,#2b3550)}
  .agent-info{font-size:10px;font-weight:600;line-height:1.35}
  .script{font-family:"Allura",cursive;font-size:26px;font-weight:400;line-height:1;margin-bottom:4px}
  .badges{display:flex;gap:6px;margin:6px 0}
  .badge{width:16px;height:16px;background:var(--ink)}
  .brand{display:flex;align-items:center;gap:5px;font-size:13px;font-weight:600;color:var(--red);margin:6px 0 4px}
  .brand .mark{width:12px;height:12px;background:var(--red)}
  .contact{font-size:11px;font-weight:700}
  .bullets{list-style:none;font-size:9px;font-weight:500;line-height:1.3}
  .bullets li{position:relative;padding-left:12px;margin-bottom:7px}
  .bullets li::before{content:"";position:absolute;left:0;top:3px;width:6px;height:6px;background:var(--blue-light)}
  .example{position:absolute;top:590px;left:0;width:100%;text-align:center}
  .example-tag{display:inline-block;background:var(--blue);color:var(--white);font-weight:700;font-size:13px;padding:2px 14px}
  .example-box{margin:0 auto;width:250px;border:2px solid var(--blue-deep);background:var(--white);font-size:12px;font-weight:700;padding:3px 0;line-height:1.3}
  .example-box span{color:var(--blue)}
  .note{font-size:7px;font-style:italic;text-align:right;width:250px;margin:3px auto 0}
  .quote{position:absolute;top:680px;left:24px;right:18px;font-size:10.5px;font-style:italic;font-weight:500;text-align:center;line-height:1.3}
  .quote::before{content:"\201C";position:absolute;left:-12px;top:-10px;font-size:30px;color:var(--blue-light);font-style:normal}
  .quote .sig{display:block;text-align:right;font-family:"Allura",cursive;font-style:normal;font-size:16px;margin-top:2px}
  .quote .cred{display:block;text-align:right;font-size:6px;font-style:normal}
  .back-contact{position:absolute;top:790px;left:20px;right:16px;display:flex;justify-content:space-between;align-items:center}
  .fineprint{position:absolute;top:835px;left:30px;right:30px;border:1px solid var(--ink);border-radius:4px;font-size:6.5px;font-style:italic;text-align:center;padding:3px 6px}
</style>
</head>
<body>
  <article class="hanger hanger--front">
    <div class="sky"></div>
    <div class="hole"></div>
    <div class="photo" role="img" aria-label="Photo of a new brick two-storey home at dusk with landscaped lawn"></div>
    <section class="band">
      <div class="headline">
        <span class="big">AWE</span>
        <span class="stack"><span class="small">and then</span><span class="big">SOME</span></span>
      </div>
      <p class="offer">Receive a minimum of</p>
      <div class="offer-row">
        <span class="offer-pct">2.5%</span>
        <span class="offer-text">or more to put<br>towards your<br><strong>NEW CONSTRUCTION</strong> home!</span>
      </div>
    </section>
    <section class="savings">
      <span class="pill">Maximize Your Savings!</span>
      <p>My <em><b>Buy &amp; List</b></em> package offers a <span class="accent">FLAT<br>FEE</span> on the sale of your current home.</p>
      <p class="label">SAVING YOU</p>
    </section>
    <section class="agent">
      <div class="portrait" role="img" aria-label="Portrait photo of the agent"></div>
      <div class="agent-info">
        <div class="script">Marla Ashcombe</div>
        REALTOR®,<br>CRS, ABR, CNHS, CHMS
        <div class="badges"><span class="badge"></span><span class="badge"></span></div>
        <div class="brand"><span class="mark"></span>Harwood Fenn</div>
        <div class="contact">555.014.2290</div>
        <div class="contact">marla.ashcombe@mailbox.net</div>
      </div>
    </section>
  </article>

  <article class="hanger hanger--back">
    <div class="photo" role="img" aria-label="Photo of a white new-construction home with a walkway and green lawn at sunset"></div>
    <div class="hole"></div>
    <section class="band">
      <ul class="bullets">
        <li>We work with 100's of builders in the local area so you are not limited to a few "select" builders.</li>
        <li>Homebuilders have the same bottom line sales price whether you have a REALTOR® representing you or not.</li>
        <li>Rebate program will not affect the price you pay for your home. Brokerage fees are paid through a separate marketing fund, not from the sales price of your home.</li>
        <li>Rebate program is in ADDITION to any builder or lender incentives.</li>
      </ul>
    </section>
    <section class="example">
      <span class="example-tag">For Example:</span>
      <div class="example-box">
        <span>$400,000</span> equals a <span>$10,000</span> rebate!<br>
        <span>$500,000</span> equals a <span>$12,500</span> rebate!
      </div>
      <p class="note">*Lender approval required</p>
    </section>
    <blockquote class="quote">
      I've sold hundreds of homes in the North Dallas area over the last 13 years, specializing in new construction homes. I would love to help you make your new home dreams a reality.
      <span class="sig">Marla Ashcombe</span>
      <span class="cred">REALTOR®, CRS, ABR, CNHS, CHMS</span>
    </blockquote>
    <div class="back-contact">
      <div class="brand"><span class="mark"></span>Harwood Fenn</div>
      <div>
        <div class="contact">555.014.2290</div>
        <div class="contact">marla.ashcombe@mailbox.net</div>
      </div>
    </div>
    <p class="fineprint">Not intended to solicit homes already listed for sale or buyers already in a buyers agency agreement with another brokerage.</p>
  </article>
</body>
</html>
```